KORVAL RENOVATIONS AND CUSTOM BUILDS

5pages:
Home/ who we are , services offered, why us,
recent projects/ gallery , contact us

Industry/Entity Type

Design, renovations, project management

Coding

Coded - Design and coding required

Number of Pages Required

5+ page

Requirements
Should not have
• Too many colours

```html
<!DOCTYPE html>
<html lang="en">
<head>
<meta charset="utf-8">
<title>Korval Renovations and Custom Builds</title>
<link href="https://fonts.googleapis.com/css2?family=Poppins:wght@300;400;500;600;700&display=swap" rel="stylesheet">
<style>
:root{
  --navy:#2f3e5c;
  --navy-dark:#27344f;
  --green:#7ab51d;
  --ink:#333c4e;
  --muted:#5c6370;
  --light:#f4f6f8;
  --pale:#f6f9f1;
  --white:#ffffff;
}
*{margin:0;padding:0;box-sizing:border-box}
html,body{width:1200px;height:3750px;overflow:hidden}
body{position:relative;font-family:'Poppins',sans-serif;color:var(--ink);background:var(--white)}
section,header,footer{position:absolute;left:0;width:1200px}
.abs{position:absolute}
.btn{position:absolute;background:var(--navy);color:var(--white);font-size:13px;display:flex;align-items:center;justify-content:center;border-bottom:2px solid var(--green)}
.photo{position:absolute}
.social{width:34px;height:34px;border-radius:50%;border:1.5px solid var(--navy);position:absolute}
.social.filled{background:var(--green);border-color:var(--green)}
.social.filled::after{content:"";position:absolute;left:10px;top:10px;width:11px;height:11px;border:1.5px solid #fff;border-radius:3px}

/* header */
.site-header{top:0;height:74px;background:var(--white)}
.brand{position:absolute;left:60px;top:16px;color:var(--navy);font-weight:500;font-size:15px;line-height:18px}
.brand small{display:block;font-size:7px;letter-spacing:2px;color:var(--green);font-weight:500}
.nav a{position:absolute;top:28px;font-size:13px;color:var(--ink);text-decoration:none;transform:translateX(-50%)}
.nav a.active{color:var(--green)}
.call{left:831px;top:20px;width:97px;height:38px;font-size:13px;gap:6px}

/* hero */
.hero{top:74px;height:560px}
.hero .photo{inset:0;background:linear-gradient(120deg,#8b8f94 0%,#c9cbcc 35%,#e4e4e2 60%,#6c6f74 100%)}
.hero .shade{position:absolute;inset:0;background:rgba(40,44,52,.25)}
.hero h1{position:absolute;top:144px;width:100%;text-align:center;color:var(--white);font-size:50px;line-height:64px;font-weight:700}
.hero h1 span{font-weight:400}
.hero p{position:absolute;top:285px;left:300px;width:600px;text-align:center;color:var(--white);font-size:12.5px;line-height:21px;font-weight:300}
.hero .btn{left:526px;top:360px;width:148px;height:36px}
.dots{position:absolute;top:466px;left:576px;display:flex;gap:10px;align-items:center}
.dots i{width:7px;height:7px;border-radius:50%;background:#fff;display:block}
.dots i.on{width:11px;height:11px;border:1.5px solid var(--green);background:transparent;position:relative}
.dots i.on::after{content:"";position:absolute;left:2px;top:2px;width:4px;height:4px;border-radius:50%;background:var(--green)}

/* proposal band */
.proposal{top:634px;height:100px;background:var(--navy)}
.proposal h3{position:absolute;top:13px;width:100%;text-align:center;color:#fff;font-size:16px;font-weight:600}
.proposal h3 span{font-weight:400}
.field{position:absolute;top:45px;height:33px;background:#fff;border:1px solid #cfd3da;display:flex;align-items:center;gap:8px;padding-left:12px;font-size:12.5px;color:var(--ink)}
.field svg{width:16px;height:16px;stroke:var(--navy);fill:none;stroke-width:1.5}
.submit{position:absolute;left:989px;top:45px;width:151px;height:33px;background:var(--green);color:#fff;font-size:13px;display:flex;align-items:center;justify-content:center}

/* who */
.who{top:734px;height:542px}
.who .photo{left:60px;top:83px;width:525px;height:374px;background:linear-gradient(135deg,#d9d3c6 0%,#b6ad9f 40%,#8a8581 70%,#c2c4c5 100%)}
.arrow{position:absolute;top:172px;width:34px;height:34px;display:flex;align-items:center;justify-content:center}
.arrow svg{width:14px;height:14px;stroke:#fff;fill:none;stroke-width:2}
.tag{position:absolute;left:324px;top:306px;width:173px;height:34px;background:#fff;font-size:13px;display:flex;align-items:center;justify-content:center}
.section-title{font-size:34px;color:var(--navy);font-weight:700;letter-spacing:.5px}
.section-title span{font-weight:400}
.who .section-title{position:absolute;left:652px;top:114px}
.who p{position:absolute;left:652px;top:163px;width:445px;font-size:12.5px;line-height:21px;color:var(--muted)}
.who .btn{left:649px;top:387px;width:105px;height:36px}

/* services */
.services{top:1276px;height:541px;background:var(--light)}
.services .section-title{position:absolute;top:46px;width:100%;text-align:center}
.card{position:absolute;top:112px;width:252px;height:301px;background:#fff}
.card .photo{left:0;top:0;width:252px;height:246px}
.card h4{position:absolute;top:258px;width:100%;text-align:center;font-size:15.5px;font-weight:500;color:var(--ink)}
.card.active{background:var(--navy-dark)}
.card.active .frame{position:absolute;inset:8px;border:1.5px solid var(--green)}
.card.active h4{top:55px;color:#fff}
.card.active p{position:absolute;top:90px;left:22px;width:208px;text-align:center;color:#fff;font-size:12.5px;line-height:21px;font-weight:300}
.card.active .more{position:absolute;left:73px;top:215px;width:105px;height:36px;background:#fff;color:var(--navy);font-size:12.5px;display:flex;align-items:center;justify-content:center}
.services .btn{left:531px;top:451px;width:138px;height:36px}

/* meaning */
.meaning{top:1817px;height:456px;background:linear-gradient(90deg,#3a4966 0%,#33425f 45%,var(--navy) 100%)}
.ring{position:absolute;left:136px;top:64px;width:330px;height:330px;border-radius:50%;border:2px solid var(--green)}
.meaning .photo{left:147px;top:75px;width:308px;height:308px;border-radius:50%;background:linear-gradient(160deg,#e5e5e3 0%,#bdbcb8 55%,#6e6151 100%)}
.meaning .section-title{position:absolute;left:620px;top:86px;color:#fff;font-size:32px}
.meaning p{position:absolute;color:#fff;font-size:12.5px;line-height:21px;font-weight:300}
.meaning .lead{left:620px;top:138px;width:480px}
.bullet{position:absolute;left:624px;color:var(--green);font-size:16px;display:flex;align-items:center;gap:14px}
.bullet::before{content:"";width:5px;height:5px;border-radius:50%;background:var(--green)}

/* why */
.why{top:2273px;height:431px}
.why .section-title{position:absolute;top:74px;width:100%;text-align:center}
.feature{position:absolute;top:142px;width:210px;text-align:center;transform:translateX(-50%)}
.feature .icon{width:82px;height:82px;margin:0 auto;border-radius:50%;background:var(--green);display:flex;align-items:center;justify-content:center}
.feature .icon svg{width:62px;height:62px;fill:none;stroke:#fff;stroke-width:1.6}
.feature h4{margin-top:12px;font-size:16px;font-weight:500;line-height:23px;color:var(--navy)}
.feature p{margin-top:2px;font-size:12.5px;line-height:21px;color:var(--muted)}

/* projects */
.projects{top:2704px;height:732px;background:var(--pale)}
.projects .section-title{position:absolute;top:56px;width:100%;text-align:center}
.projects .photo{width:345px}
.overlay{position:absolute;left:427px;top:330px;width:345px;height:262px;background:rgba(39,52,79,.88)}
.overlay .frame{position:absolute;inset:14px;border:1.5px solid var(--green)}
.overlay .plus{position:absolute;left:157px;top:98px;width:30px;height:30px}
.overlay h4{position:absolute;top:140px;width:100%;text-align:center;color:#fff;font-size:16px;font-weight:600}
.projects .btn{left:552px;top:637px;width:96px;height:36px}

/* footer */
.site-footer{top:3436px;height:314px;background:var(--navy);color:#fff}
.site-footer .brand{top:74px;color:#fff;font-size:18px;line-height:22px}
.site-footer .brand small{color:#fff;font-size:8px;letter-spacing:3px}
.site-footer .about{position:absolute;left:60px;top:158px;width:200px;font-size:12px;line-height:22px;font-weight:300}
.col-title{position:absolute;top:76px;font-size:13px;color:var(--green)}
.links a{position:absolute;left:334px;font-size:12px;color:#fff;text-decoration:none}
.contact-row{position:absolute;left:613px;display:flex;gap:12px;font-size:12px;line-height:18px;align-items:flex-start}
.contact-row svg{width:18px;height:18px;fill:none;stroke:var(--green);stroke-width:1.5;flex:none}
.site-footer .social{border-color:#fff}
.site-footer .social.filled{border-color:var(--green)}
.rule{position:absolute;left:0;top:270px;width:1200px;height:1px;background:rgba(255,255,255,.18)}
.copy{position:absolute;top:285px;width:100%;text-align:center;font-size:12px;font-weight:300}
</style>
</head>
<body>

<header class="site-header">
  <div class="brand">KORVAL<br>RENOVATIONS<small>AND CUSTOM BUILDS</small></div>
  <nav class="nav">
    <a class="active" style="left:371px">Home</a>
    <a style="left:485px">Services Offered</a>
    <a style="left:626px">Recent Projects</a>
    <a style="left:751px">Contact Us</a>
  </nav>
  <div class="btn call"><svg width="16" height="16" viewBox="0 0 24 24" fill="#fff"><path d="M6.6 10.8a15 15 0 0 0 6.6 6.6l2.2-2.2c.3-.3.7-.4 1-.2 1.1.4 2.3.6 3.6.6.6 0 1 .4 1 1V20c0 .6-.4 1-1 1A17 17 0 0 1 3 4c0-.6.4-1 1-1h3.5c.6 0 1 .4 1 1 0 1.3.2 2.5.6 3.6.1.3 0 .7-.2 1z"/></svg>Call Us</div>
  <span class="social filled" style="left:961px;top:20px" role="img" aria-label="Social profile"></span>
  <span class="social" style="left:1009px;top:20px" role="img" aria-label="Social profile"></span>
  <span class="social" style="left:1056px;top:20px" role="img" aria-label="Social profile"></span>
  <span class="social" style="left:1103px;top:20px" role="img" aria-label="Social profile"></span>
</header>

<section class="hero">
  <div class="photo" role="img" aria-label="Renovated kitchen with white marble countertop, dark cabinets and window"></div>
  <div class="shade"></div>
  <h1>KORVAL RENOVATIONS AND<br><span>CUSTOM BUILDS</span></h1>
  <p>Lorem Ipsum is simply dummy text of the printing and typesetting industry. Lorem Ipsum has been the industry's standard dummy text</p>
  <div class="btn">Contact Us Today</div>
  <div class="dots"><i></i><i class="on"></i><i></i></div>
</section>

<section class="proposal">
  <h3>Fill out form and receive a <span>Free Proposal Withing 24 hours</span></h3>
  <div class="field" style="left:60px;width:202px"><svg viewBox="0 0 24 24"><circle cx="12" cy="8" r="4"/><path d="M4 21c0-4 4-7 8-7s8 3 8 7"/></svg>Full Name</div>
  <div class="field" style="left:281px;width:224px"><svg viewBox="0 0 24 24"><rect x="3" y="6" width="18" height="12"/><path d="M3 6l9 7 9-7"/></svg>Email</div>
  <div class="field" style="left:520px;width:212px"><svg viewBox="0 0 24 24"><path d="M6.6 10.8a15 15 0 0 0 6.6 6.6l2.2-2.2 4.6 1.4V20A17 17 0 0 1 4 4h3.6l1.2 4.6z"/></svg>Phone No.</div>
  <div class="field" style="left:748px;width:225px"><svg viewBox="0 0 24 24"><rect x="3" y="4" width="18" height="13"/><path d="M7 9h10M7 12h6M8 17l-2 4"/></svg>Massage</div>
  <div class="submit">Chat Free Request</div>
</section>

<section class="who">
  <div class="photo" role="img" aria-label="Residential living room with sofa, chandelier and wall-mounted TV"></div>
  <div class="arrow" style="left:60px;background:var(--navy)"><svg viewBox="0 0 24 24"><path d="M15 4l-8 8 8 8"/></svg></div>
  <div class="arrow" style="left:551px;background:var(--green)"><svg viewBox="0 0 24 24"><path d="M9 4l8 8-8 8"/></svg></div>
  <div class="tag">Residential Renovation</div>
  <h2 class="section-title">WHO <span>WE ARE</span></h2>
  <p>Lorem Ipsum is simply dummy text of the printing and typesetting industry. Lorem Ipsum has been the industry's standard dummy text ever since the 1500s, when an unknown printer took a galley of type and scrambled it to make a type specimen book. It has survived not only five centuries, but also the leap into electronic typesetting, remaining essentially unchanged. It was popularised in the 1960s with the release of Letraset sheets containing Lorem Ipsum passages, and more recently with desktop publishing software like Aldus PageMaker including versions of Lorem Ipsum.</p>
  <div class="btn">Learn More</div>
</section>

<section class="services">
  <h2 class="section-title">SERVICES <span>&nbsp;OFFERED</span></h2>
  <div class="card" style="left:60px">
    <div class="photo" role="img" aria-label="Finished basement with black marble walls and glossy floor" style="background:linear-gradient(150deg,#2a2b2e 0%,#6d6e70 45%,#1c1d20 100%)"></div>
    <h4>Finishing basements</h4>
  </div>
  <div class="card active" style="left:336px">
    <div class="frame"></div>
    <h4>Second Legal Units</h4>
    <p>Lorem Ipsum is simply dummy text of the printing and typesetting industry. Lorem Ipsum has been the industry's standard dummy text.</p>
    <div class="more">Learn More</div>
  </div>
  <div class="card" style="left:612px">
    <div class="photo" role="img" aria-label="Remodeled room with grey closet doors and wood floor" style="background:linear-gradient(180deg,#e6e6e4 0%,#9a968f 55%,#5b554d 100%)"></div>
    <h4>Complete Remodeling</h4>
  </div>
  <div class="card" style="left:888px">
    <div class="photo" role="img" aria-label="Exterior basement walkout addition with railings beside brick wall" style="background:linear-gradient(160deg,#7d7a6f 0%,#9e7a5d 45%,#6f6a64 100%)"></div>
    <h4>Extensions / Additions</h4>
  </div>
  <div class="btn">View All Services</div>
</section>

<section class="meaning">
  <div class="ring"></div>
  <div class="photo" role="img" aria-label="Renovated basement room with white walls and wood-look floor"></div>
  <h2 class="section-title">WHAT THIS <span>REALLY MEANS</span></h2>
  <p class="lead">Lorem Ipsum is simply dummy text of the printing and typesetting industry. Lorem Ipsum has been the industry's standard dummy text ever since the 1500s, when an unknown printer took a galley of type</p>
  <div class="bullet" style="top:222px">Our team does:</div>
  <p style="left:646px;top:252px;width:450px">demolition, cutting doors/ windows, framing, thermal insulation, fire separation, drywalling, painting, flooring, doors, trims, kitchen cabinets</p>
  <div class="bullet" style="top:334px">Our subcontractors do:</div>
</section>

<section class="why">
  <h2 class="section-title">WHY <span>US</span></h2>
  <div class="feature" style="left:159px">
    <div class="icon"><svg viewBox="0 0 64 64"><circle cx="32" cy="32" r="26"/><circle cx="32" cy="28" r="12"/><path d="M32 21l2.2 4.6 5 .6-3.7 3.4 1 5-4.5-2.5-4.5 2.5 1-5-3.7-3.4 5-.6z"/><path d="M24 38l-4 10 6-2 3 5 3-9M40 38l4 10-6-2-3 5-3-9"/></svg></div>
    <h4>Competitive Rates</h4>
    <p>Lorem Ipsum is simply dummy text of the printing and typesetting industry.</p>
  </div>
  <div class="feature" style="left:380px">
    <div class="icon"><svg viewBox="0 0 64 64"><circle cx="32" cy="32" r="26"/><rect x="17" y="21" width="30" height="22" rx="2"/><path d="M17 27h30"/><rect x="22" y="31" width="8" height="8"/><path d="M38 30l-3 5h4l-3 5"/></svg></div>
    <h4>Licensed<br>subcontractors</h4>
    <p>Lorem Ipsum is simply dummy text of the printing and typesetting industry.</p>
  </div>
  <div class="feature" style="left:600px">
    <div class="icon"><svg viewBox="0 0 64 64"><circle cx="32" cy="32" r="26"/><circle cx="32" cy="32" r="15"/><path d="M17 32h30M32 17c-6 8-6 22 0 30M32 17c6 8 6 22 0 30"/></svg></div>
    <h4>Wide network of<br>consultants</h4>
    <p>Lorem Ipsum is simply dummy text of the printing and typesetting industry.</p>
  </div>
  <div class="feature" style="left:820px">
    <div class="icon"><svg viewBox="0 0 64 64"><circle cx="32" cy="32" r="26"/><circle cx="30" cy="30" r="13"/><path d="M30 17v13h13M30 30l9 9"/><path d="M38 40h10M38 44h10M38 48h10"/></svg></div>
    <h4>Suppliers list suits<br>every budget</h4>
    <p>Lorem Ipsum is simply dummy text of the printing and typesetting industry.</p>
  </div>
  <div class="feature" style="left:1038px">
    <div class="icon"><svg viewBox="0 0 64 64"><circle cx="32" cy="32" r="26"/><circle cx="29" cy="29" r="13"/><path d="M29 21v8l5 4"/><circle cx="41" cy="39" r="4"/><path d="M33 50c1-4 4-6 8-6s7 2 8 6"/></svg></div>
    <h4>Flexible working<br>hours</h4>
    <p>Lorem Ipsum is simply dummy text of the printing and typesetting industry.</p>
  </div>
</section>

<section class="projects">
  <h2 class="section-title">RECENT <span>PROJECTS</span></h2>
  <div class="photo" role="img" aria-label="Basement room with grey walls and wood-look floor" style="left:60px;top:126px;height:263px;background:linear-gradient(150deg,#8a8f93 0%,#b4b4b0 40%,#5d4c3e 100%)"></div>
  <div class="photo" role="img" aria-label="Renovated room with tall grey closet doors" style="left:60px;top:406px;height:186px;background:linear-gradient(180deg,#deddda 0%,#7f7a72 60%,#4a4038 100%)"></div>
  <div class="photo" role="img" aria-label="Framed interior walls during construction" style="left:427px;top:126px;height:187px;background:linear-gradient(90deg,#c8a77e 0%,#5c4e47 45%,#c9b08c 100%)"></div>
  <div class="photo" role="img" aria-label="Finished kitchen with dark cabinets" style="left:427px;top:330px;height:262px;background:linear-gradient(160deg,#8b8d90 0%,#4f535a 100%)"></div>
  <div class="overlay">
    <div class="frame"></div>
    <svg class="plus" viewBox="0 0 30 30"><path d="M15 2v26M2 15h26" stroke="#7ab51d" stroke-width="2.5"/></svg>
    <h4>Project Name</h4>
  </div>
  <div class="photo" role="img" aria-label="White panel closet doors in finished hallway" style="left:795px;top:126px;height:263px;background:linear-gradient(90deg,#cfcfcc 0%,#efefed 40%,#d9d9d6 100%)"></div>
  <div class="photo" role="img" aria-label="Exterior basement walkout with wooden railings" style="left:795px;top:406px;height:186px;background:linear-gradient(160deg,#7d7a6f 0%,#9e7a5d 45%,#6f6a64 100%)"></div>
  <div class="btn">See More</div>
</section>

<footer class="site-footer">
  <div class="brand">KORVAL<br>RENOVATIONS<small>AND CUSTOM BUILDS</small></div>
  <p class="about">Lorem ipsum dolor sit amet, consectetur adipiscing elit, sed do eiusmod tempor...</p>
  <div class="col-title" style="left:332px">Site Map</div>
  <nav class="links">
    <a style="top:108px">Home</a>
    <a style="top:139px">Services Offered</a>
    <a style="top:170px">Recent Projects</a>
    <a style="top:203px">Contact Us</a>
  </nav>
  <div class="col-title" style="left:613px">Contact Us</div>
  <div class="contact-row" style="top:106px"><svg viewBox="0 0 24 24"><path d="M12 22s7-7 7-12a7 7 0 0 0-14 0c0 5 7 12 7 12z"/><circle cx="12" cy="10" r="2.5"/></svg><span>123 Lorem Ipsum Is A<br>dummy text.</span></div>
  <div class="contact-row" style="top:161px;font-weight:600"><svg viewBox="0 0 24 24"><path d="M6.6 10.8a15 15 0 0 0 6.6 6.6l2.2-2.2 4.6 1.4V20A17 17 0 0 1 4 4h3.6l1.2 4.6z"/></svg><span>(555)014-2277</span></div>
  <div class="contact-row" style="top:204px"><svg viewBox="0 0 24 24"><rect x="3" y="6" width="18" height="12"/><path d="M3 6l9 7 9-7"/></svg><span>info@korvalbuilds.com</span></div>
  <div class="col-title" style="left:890px">Follow On Us</div>
  <span class="social filled" style="left:890px;top:110px" role="img" aria-label="Social profile"></span>
  <span class="social" style="left:944px;top:110px" role="img" aria-label="Social profile"></span>
  <span class="social" style="left:999px;top:110px" role="img" aria-label="Social profile"></span>
  <span class="social" style="left:1053px;top:110px" role="img" aria-label="Social profile"></span>
  <div class="rule"></div>
  <div class="copy">2022© KORVAL RENOVATIONS AND CUSTOM BUILDS. All right reserved.</div>
</footer>

</body>
</html>
```